Redesign Of Flower Delivery Subscription Service Website

I need a revamped website of www.petal-rush.com

Please revamp current design using same content....

Target Market(s)

people who buy flowers. Brides, wedding planners, wedding photographer, married man, boyfriend, etc.

Industry/Entity Type

Florist

Number of Pages Required

5+ page

Colors

Designer to choose colors to be used in the design.

Requirements
Must have
• I need a revamped website of www.petal-rush.com
• Please revamp current design using same content....
Nice to have
Should not have

```html
<!DOCTYPE html>
<html lang="en">
<head>
<meta charset="utf-8">
<title>PetalRush – Monthly Flower Delivery</title>
<link href="https://fonts.googleapis.com/css2?family=Open+Sans:ital,wght@0,400;0,600;0,700;1,400;1,600;1,700&family=Yesteryear&display=swap" rel="stylesheet">
<style>
:root{
  --blue:#2f93e0;
  --blue-dark:#1f7fd0;
  --pink-band:#ef86a6;
  --pink-band-dark:#e2708f;
  --gold:#e6b55c;
  --gold-soft:#f0cc85;
  --rose:#e6a6d9;
  --rose-light:#f4c8e8;
  --plum:#9b2a8c;
  --rust:#c2471c;
  --berry:#a33a3a;
  --white:#ffffff;
  --ink:#222;
  --text:#333;
  --leaf:#3f8a3a;
}
*{box-sizing:border-box;margin:0;padding:0}
html,body{width:1200px;height:2510px;overflow:hidden}
body{position:relative;font-family:"Open Sans",Arial,sans-serif;color:var(--ink);background:var(--white)}
.abs{position:absolute}

/* hero */
.hero{left:0;top:0;width:1200px;height:620px;background:linear-gradient(180deg,#d3e8f6 0%,#bddbef 40%,#a6c8c6 68%,#b7d5e6 100%)}
.brand{left:40px;top:40px;font-size:40px;font-weight:700;color:var(--leaf);letter-spacing:.5px;line-height:1.3}
.nav a{position:absolute;font-size:19px;line-height:1.3;color:var(--blue);text-decoration:none;white-space:nowrap}
.cart{left:1066px;top:20px;width:106px;height:93px;background:var(--blue);border:3px solid #e9f4fc;border-radius:6px;display:flex;align-items:center;justify-content:center}
.hanging-basket{left:36px;top:126px;width:540px;height:414px;border-radius:30px;background:linear-gradient(160deg,rgba(240,106,142,.75) 0%,rgba(243,138,167,.7) 45%,rgba(130,170,120,.5) 80%,rgba(185,217,238,0) 100%)}
.hero-title{left:560px;top:175px;width:590px;text-align:center;font-family:"Yesteryear",cursive;font-weight:400;font-size:84px;color:var(--blue);line-height:1}
.hero-sub{left:560px;width:590px;text-align:center;font-style:italic;font-size:18px;line-height:1.3;color:var(--blue)}
.perk-icon{top:388px;height:116px;width:80px}
.perk{top:515px;width:190px;height:40px;border:3px solid var(--white);border-radius:8px;background:rgba(255,255,255,.45);color:var(--blue-dark);font-size:18px;text-align:center;line-height:34px}

/* upgrade band */
.upgrade{left:0;top:620px;width:1200px;height:262px;background:repeating-linear-gradient(180deg,var(--pink-band) 0 44px,var(--pink-band-dark) 44px 46px)}
.upgrade-box{left:239px;top:668px;width:722px;height:164px;background:rgba(160,70,90,.28);border-radius:10px}
.upgrade-label{left:239px;top:690px;width:722px;text-align:center;font-style:italic;font-size:18px;line-height:1.3;color:#fbe6ee;letter-spacing:.5px}
.email-field{left:265px;top:736px;width:669px;height:74px;border:4px solid var(--white);border-radius:12px;background:rgba(255,255,255,.25);text-align:center;line-height:66px;font-size:15px;color:#b0305a}
.arrow{top:742px;width:30px;height:50px}

/* features */
.features{left:0;top:882px;width:1200px;height:640px;background:linear-gradient(135deg,var(--gold-soft),var(--gold) 60%,#d9a44a)}
.photo-frame{top:923px;width:299px;height:348px;background:var(--white);padding:9px}
.photo{width:100%;height:100%}
.feature-card{top:1327px;width:327px;height:108px;border:3px solid var(--white);border-radius:10px;background:rgba(255,235,205,.55);text-align:center;padding:4px 12px 0;overflow:hidden}
.feature-card h3{font-family:"Yesteryear",cursive;font-weight:400;font-size:26px;line-height:32px;white-space:nowrap}
.feature-card p{font-size:13.5px;line-height:21px;color:var(--text);height:42px;overflow:hidden}
.read-more{font-family:"Yesteryear",cursive;font-size:20px;line-height:22px}

/* about */
.about{left:0;top:1522px;width:1200px;height:670px;background:linear-gradient(120deg,var(--rose-light) 0%,var(--rose) 55%,#eec3e2 85%,#f3d6ea 100%)}
.about-box{left:31px;top:1638px;width:689px;height:283px;border:3px solid var(--white);border-radius:8px;background:rgba(255,240,250,.55);padding:10px 14px 0;text-align:center}
.about-box h2{font-family:"Yesteryear",cursive;font-weight:400;font-size:27px;color:var(--plum);line-height:36px}
.about-box p{font-size:12.6px;line-height:18.5px;margin-top:10px;padding:0 12px;color:var(--ink)}
.about-box .read-more{display:block;margin-top:4px;color:var(--plum)}

/* footer */
.footer{left:0;top:2192px;width:1200px;height:318px;background:linear-gradient(100deg,#bcd7ea 0%,#d9e6f0 40%,#e9c7dc 70%,#cfe0ee 100%)}
.footer-brand{left:40px;top:2324px;font-size:40px;font-weight:700;color:var(--leaf);line-height:1.3}
.copyright{left:40px;top:2424px;width:230px;text-align:center;font-size:14px;font-weight:700;line-height:24px;color:var(--ink)}
.footer-heading{font-style:italic;font-weight:700;font-size:17px;line-height:1.3;color:var(--blue)}
.footer-text{font-size:13.5px;line-height:22px;color:var(--text);white-space:nowrap}
.footer-icon{width:18px;height:18px}
</style>
</head>
<body>

<section class="abs hero" aria-label="Hero"></section>
<div class="abs hanging-basket" role="img" aria-label="Photo of a hanging basket of pink petunias"></div>
<div class="abs brand">PetalRush</div>

<nav class="nav">
  <a style="left:286px;top:28px">Home</a>
  <a style="left:389px;top:28px">How it Works</a>
  <a style="left:545px;top:28px">Free Flowers Monthly</a>
  <a style="left:776px;top:28px">Delivery Areas</a>
  <a style="left:941px;top:28px">Help</a>
  <a style="left:324px;top:75px">Franchise</a>
  <a style="left:443px;top:75px">Corporate Arrangements</a>
  <a style="left:709px;top:75px">My Account</a>
  <a style="left:866px;top:75px">Blogs</a>
</nav>

<div class="abs cart" aria-label="Shopping cart">
  <svg width="60" height="56" viewBox="0 0 60 56" fill="none" stroke="#fff" stroke-width="4" stroke-linejoin="round" stroke-linecap="round">
    <path d="M4 10h8l6 26h30l6-18H16"/>
    <circle cx="22" cy="46" r="4" fill="#fff"/>
    <circle cx="44" cy="46" r="4" fill="#fff"/>
  </svg>
</div>

<h1 class="abs hero-title">Always Fresh</h1>
<p class="abs hero-sub" style="top:290px">Beautiful Flower Arrangements Delivered Monthly</p>
<p class="abs hero-sub" style="top:330px">Now only $69.95/MTH ($100 value)</p>

<svg class="abs perk-icon" style="left:545px" viewBox="0 0 80 116" aria-label="Vase icon"><path d="M28 4h24v10c0 6 14 18 14 48 0 26-12 50-26 50S14 88 14 62c0-30 14-42 14-48z" fill="#fff"/></svg>
<svg class="abs perk-icon" style="left:779px" viewBox="0 0 80 116" aria-label="Bouquet icon"><circle cx="40" cy="28" r="22" fill="#fff"/><path d="M22 48h36L46 110H34z" fill="#fff"/></svg>
<svg class="abs perk-icon" style="left:1021px;width:90px" viewBox="0 0 90 116" aria-label="Gift icon"><rect x="6" y="40" width="78" height="20" fill="#fff"/><rect x="12" y="64" width="66" height="44" fill="#fff"/><path d="M45 40c-10-16-28-20-28-8s18 8 28 8c10 0 28 4 28-8s-18-8-28 8z" fill="none" stroke="#fff" stroke-width="5"/></svg>

<div class="abs perk" style="left:491px">Free Vase</div>
<div class="abs perk" style="left:725px">Free Delivery</div>
<div class="abs perk" style="left:979px">Free Upgrade</div>

<section class="abs upgrade" aria-label="Free upgrade sign-up"></section>
<div class="abs upgrade-box"></div>
<p class="abs upgrade-label">Enter Your Email To Receive A FREE UPGRADE</p>
<div class="abs email-field">Email Address</div>
<svg class="abs arrow" style="left:44px" viewBox="0 0 30 50"><path d="M24 6L8 25l16 19" fill="none" stroke="#6a5560" stroke-width="6"/></svg>
<svg class="abs arrow" style="left:1128px" viewBox="0 0 30 50"><path d="M6 6l16 19L6 44" fill="none" stroke="#6a5560" stroke-width="6"/></svg>

<section class="abs features" role="img" aria-label="Photo backdrop of yellow chrysanthemums"></section>

<div class="abs photo-frame" style="left:63px"><div class="photo" role="img" aria-label="Photo of peach roses in a red vase" style="background:linear-gradient(180deg,#f6efe9 0%,#e9a48c 40%,#b9866a 70%,#f4f1ee 100%)"></div></div>
<div class="abs photo-frame" style="left:450px"><div class="photo" role="img" aria-label="Photo of cream and burgundy roses in a glass vase" style="background:linear-gradient(180deg,#ede5d6 0%,#e6d3bf 40%,#b08a8e 70%,#e9e6e0 100%)"></div></div>
<div class="abs photo-frame" style="left:839px"><div class="photo" role="img" aria-label="Photo of purple stock and roses in a vase with a lavender bow" style="background:linear-gradient(180deg,#d8dde2 0%,#9a6fb0 35%,#8aa06a 65%,#c2ccd4 100%)"></div></div>

<div class="abs feature-card" style="left:49px">
  <h3 style="color:var(--rust)">Set It And Forget It</h3>
  <p>PetalRush is a "SET IT and FORGET IT" subscription based flower delivery</p>
  <div class="read-more" style="color:var(--rust)">Read More</div>
</div>
<div class="abs feature-card" style="left:436px">
  <h3 style="color:var(--rust)">But Never Forget Again</h3>
  <p>When setting up your account, you can choose exact delivery dates for the</p>
  <div class="read-more" style="color:var(--rust)">Read More</div>
</div>
<div class="abs feature-card" style="left:823px">
  <h3 style="color:var(--berry)">Making Someone's Day Better</h3>
  <p>Be the hero in that special someone's life each and every month. It feels good</p>
  <div class="read-more" style="color:var(--berry)">Read More</div>
</div>

<section class="abs about" role="img" aria-label="Photo backdrop of a tea cup, sugar cubes and white baby's breath on pink"></section>
<div class="abs about-box">
  <h2>Monthly Subscription Based Flower Delivery Service in San Diego –<br>CA by Our Florist Shop</h2>
  <p>Every moment of life could be cherished perfectly……IF you choose wisely. To make your day more treasured, remember that flowers are the smartest choice when delivered through our monthly PetalRush subscription based delivery service. Our online subscription-based flower delivery service can help you pamper, cherish and make an everlasting impression on the minds of your loved ones with a doorstep delivery of exquisitely hand-designed floral arrangements. Our online subscription service features both standard and personalized services to help you choose from an assortment of classic and contemporary floral arrangements. It is your chance to setup a weekly, monthly, or quarterly subscription, so we can deliver the most exotic collections of hand-decorated flowers that you and your loved ones will cherish.</p>
  <span class="read-more">Read More</span>
</div>

<footer class="abs footer" role="img" aria-label="Photo backdrop of pink gerbera and white roses"></footer>
<div class="abs footer-brand">PetalRush</div>
<p class="abs copyright">Copyright © 2018.<br>All Rights Reserved.</p>

<h4 class="abs footer-heading" style="left:346px;top:2246px">Contact Info</h4>
<h4 class="abs footer-heading" style="left:621px;top:2249px">More Services</h4>

<svg class="abs footer-icon" style="left:300px;top:2336px" viewBox="0 0 18 18"><path d="M9 1a6 6 0 0 0-6 6c0 5 6 10 6 10s6-5 6-10a6 6 0 0 0-6-6z" fill="var(--blue)"/><circle cx="9" cy="7" r="2.2" fill="#fff"/></svg>
<p class="abs footer-text" style="left:335px;top:2333px">418 Larkspur Avenue,<br>San Diego CA 92101</p>

<svg class="abs footer-icon" style="left:300px;top:2401px" viewBox="0 0 18 18"><rect x="1" y="3" width="16" height="12" rx="1" fill="var(--blue)"/><path d="M1 4l8 6 8-6" fill="none" stroke="#fff" stroke-width="1.5"/></svg>
<p class="abs footer-text" style="left:335px;top:2398px">Email: hello@petalrush-mail.com</p>

<svg class="abs footer-icon" style="left:300px;top:2450px" viewBox="0 0 18 18"><path d="M4 1l3 4-2 2c1 3 3 5 6 6l2-2 4 3-2 3C7 17 1 11 1 3z" fill="var(--blue)"/></svg>
<p class="abs footer-text" style="left:335px;top:2447px">619-555-0148</p>

<p class="abs footer-text" style="left:616px;top:2333px">Corporate Arrangements<br>Hotel Arrangements<br>Events<br>Weddings</p>

<p class="abs footer-text" style="left:941px;top:2448px;font-size:13px">Privacy Policy Terms &amp; Conditions</p>

</body>
</html>
```